Dr Peter Vandell
Urologist
Professional
Dr Peter Vandell MB,ChB(UCT), FC Urol.(SA)
Ridgeway Medicentre and Lanford Private Hospital PO Box 58147 Brookvale 4105
povandell@medinet-mail.co.za
Pr No 7315824
Please email me for scanned copies of the existing stationery and cards to see current format

```html
<!DOCTYPE html>
<html lang="en">
<head>
<meta charset="utf-8">
<title>Dr Peter Vandell – Stationery</title>
<link href="https://fonts.googleapis.com/css2?family=Crimson+Text:wght@400;600;700&family=Arimo:wght@400;700&display=swap" rel="stylesheet">
<style>
  :root {
    --bg: #ece8e2;
    --paper: #ffffff;
    --brand-red: #9b1c24;
    --brand-red-dark: #7d141b;
    --ink: #222222;
    --muted: #555555;
    --rule: #9a9a9a;
    --shadow: rgba(0,0,0,0.18);
  }
  * { box-sizing: border-box; margin: 0; padding: 0; }
  html, body { width: 1200px; height: 678px; overflow: hidden; }
  body { background: var(--bg); position: relative; font-family: "Arimo", sans-serif; color: var(--ink); }

  .sheet { position: absolute; background: var(--paper); box-shadow: 0 3px 10px var(--shadow); overflow: hidden; }
  .wave { position: absolute; left: 0; width: 100%; display: block; }

  .identity { position: absolute; font-family: "Crimson Text", serif; }
  .identity .name { color: var(--brand-red); font-weight: 700; line-height: 1; }
  .identity .qualifications { color: var(--muted); font-family: "Arimo", sans-serif; letter-spacing: .04em; text-transform: uppercase; margin-top: 3px; }
  .identity .specialty { color: var(--brand-red); font-weight: 700; line-height: 1; }

  .contact { position: absolute; font-family: "Arimo", sans-serif; color: var(--ink); line-height: 1.45; }
  .contact .practice { font-weight: 700; margin-bottom: 4px; }

  .footer-line { position: absolute; font-family: "Arimo", sans-serif; }

  /* business card */
  .business-card { left: 48px; top: 365px; width: 221px; height: 139px; }
  .business-card .identity { left: 12px; top: 14px; }
  .business-card .name { font-size: 13px; }
  .business-card .qualifications { font-size: 4px; }
  .business-card .specialty { font-size: 13px; margin-top: 8px; }
  .business-card .divider { position: absolute; left: 108px; top: 12px; width: 1px; height: 70px; background: var(--rule); }
  .business-card .contact { left: 116px; top: 13px; font-size: 4.6px; width: 98px; }
  .business-card .wave { bottom: 0; height: 40px; }
  .business-card .footer-line { left: 14px; bottom: 6px; font-size: 5px; color: var(--paper); }

  /* letterhead */
  .letterhead { left: 271px; top: 108px; width: 408px; height: 521px; }
  .letterhead .identity { left: 22px; top: 22px; }
  .letterhead .name { font-size: 17px; }
  .letterhead .qualifications { font-size: 5px; }
  .letterhead .specialty { font-size: 17px; margin-top: 12px; }
  .letterhead .divider { position: absolute; left: 165px; top: 20px; width: 1px; height: 62px; background: var(--rule); }
  .letterhead .contact { left: 173px; top: 20px; font-size: 5px; width: 120px; }
  .letterhead .wave { bottom: 0; height: 66px; }
  .letterhead .footer-line { left: 26px; bottom: 9px; font-size: 6px; color: var(--paper); }

  /* envelope front */
  .envelope-front { left: 691px; top: 101px; width: 456px; height: 211px; }
  .envelope-front .identity { left: 26px; top: 22px; }
  .envelope-front .name { font-size: 19px; }
  .envelope-front .qualifications { font-size: 5px; }
  .envelope-front .specialty { font-size: 18px; margin-top: 12px; }
  .envelope-front .divider { position: absolute; left: 176px; top: 22px; width: 1px; height: 64px; background: var(--rule); }
  .envelope-front .contact { left: 184px; top: 22px; font-size: 5px; width: 120px; }
  .envelope-front .wave { top: 108px; height: 62px; }
  .envelope-front .footer-line { left: 30px; bottom: 12px; font-size: 6px; color: var(--muted); }

  /* envelope back */
  .envelope-back { left: 691px; top: 326px; width: 456px; height: 298px; }
  .envelope-back .flaps { position: absolute; inset: 0; width: 100%; height: 100%; }
  .envelope-back .identity { left: 0; width: 100%; text-align: center; }
  .envelope-back .identity.on-flap { top: 30px; }
  .envelope-back .identity.on-flap .name { color: var(--paper); font-size: 17px; }
  .envelope-back .identity.on-flap .qualifications { color: #f0d9db; font-size: 5px; }
  .envelope-back .identity.on-body { top: 198px; }
  .envelope-back .identity.on-body .name { font-size: 17px; }
  .envelope-back .identity.on-body .qualifications { font-size: 5px; }
</style>
</head>
<body>

<section class="sheet business-card" aria-label="Business card">
  <div class="identity">
    <p class="name">Dr Peter Vandell</p>
    <p class="qualifications">MB,ChB(UCT), FC Urol.(SA)</p>
    <p class="specialty">Urologist</p>
  </div>
  <div class="divider"></div>
  <div class="contact">
    <p class="practice">Ridgeway Medicentre and Lanford Private Hospital</p>
    <p>PO Box 58147 Brookvale 4105</p>
    <p>Tel 033 555 0142</p>
    <p>Fax 033 555 0143</p>
    <p>Cell 082 555 0144</p>
    <p>povandell@medinet-mail.co.za</p>
    <p>Pr No 7315824</p>
  </div>
  <svg class="wave" viewBox="0 0 221 40" preserveAspectRatio="none" aria-hidden="true">
    <path d="M0 12 C70 -2 150 28 221 4" fill="none" stroke="#111" stroke-width="1.6"/>
    <path d="M0 17 C70 4 150 34 221 9 L221 40 L0 40 Z" fill="var(--brand-red)"/>
  </svg>
  <p class="footer-line">Emergencies 082 555 0145</p>
</section>

<section class="sheet letterhead" aria-label="Letterhead">
  <div class="identity">
    <p class="name">Dr Peter Vandell</p>
    <p class="qualifications">MB,ChB(UCT), FC Urol.(SA)</p>
    <p class="specialty">Urologist</p>
  </div>
  <div class="divider"></div>
  <div class="contact">
    <p class="practice">Ridgeway Medicentre and<br>Lanford Private Hospital</p>
    <p>PO Box 58147 Brookvale 4105</p>
    <p>Tel 033 555 0142</p>
    <p>Fax 033 555 0143</p>
    <p>Cell 082 555 0144</p>
    <p>povandell@medinet-mail.co.za</p>
    <p>Pr No 7315824</p>
  </div>
  <svg class="wave" viewBox="0 0 408 66" preserveAspectRatio="none" aria-hidden="true">
    <path d="M0 22 C130 -4 270 48 408 6" fill="none" stroke="#111" stroke-width="2"/>
    <path d="M0 29 C130 6 270 58 408 14 L408 66 L0 66 Z" fill="var(--brand-red)"/>
  </svg>
  <p class="footer-line">Emergencies 082 555 0145</p>
</section>

<section class="sheet envelope-front" aria-label="Envelope front">
  <div class="identity">
    <p class="name">Dr Peter Vandell</p>
    <p class="qualifications">MB,ChB(UCT), FC Urol.(SA)</p>
    <p class="specialty">Urologist</p>
  </div>
  <div class="divider"></div>
  <div class="contact">
    <p class="practice">Ridgeway Medicentre and<br>Lanford Private Hospital</p>
    <p>PO Box 58147 Brookvale 4105</p>
    <p>Tel 033 555 0142</p>
    <p>Fax 033 555 0143</p>
    <p>Cell 082 555 0144</p>
    <p>povandell@medinet-mail.co.za</p>
  </div>
  <svg class="wave" viewBox="0 0 456 62" preserveAspectRatio="none" aria-hidden="true">
    <path d="M0 20 C140 -4 300 44 456 6" fill="none" stroke="#111" stroke-width="2"/>
    <path d="M0 27 C140 6 300 54 456 14 L456 38 C300 60 140 30 0 46 Z" fill="var(--brand-red)"/>
  </svg>
  <p class="footer-line">Emergencies 082 555 0145</p>
</section>

<section class="sheet envelope-back" aria-label="Envelope back">
  <svg class="flaps" viewBox="0 0 456 298" preserveAspectRatio="none" aria-hidden="true">
    <rect width="456" height="298" fill="#f7f7f7"/>
    <path d="M0 298 L190 150 Q228 128 266 150 L456 298 Z" fill="#ffffff" stroke="#d8d8d8" stroke-width="1"/>
    <path d="M0 0 L456 0 L456 66 L248 168 Q228 178 208 168 L0 66 Z" fill="var(--brand-red)"/>
    <path d="M0 66 L208 168 Q228 178 248 168 L456 66" fill="none" stroke="var(--brand-red-dark)" stroke-width="2"/>
  </svg>
  <div class="identity on-flap">
    <p class="name">Dr Peter Vandell</p>
    <p class="qualifications">MB,ChB(UCT), FC Urol.(SA)</p>
  </div>
  <div class="identity on-body">
    <p class="name">Dr Peter Vandell</p>
    <p class="qualifications">MB,ChB(UCT), FC Urol.(SA)</p>
  </div>
</section>

</body>
</html>
```